KJ Glimmer Cleaning Business Card

We need a business card for our new business, a cleaning company using steam. We already have a logo, and would like a modern-looking card using colors that go well with those in our logo.

```html
<!DOCTYPE html>
<html lang="en">
<head>
<meta charset="utf-8">
<title>KJ Glimmer Cleaning – Business Card</title>
<link rel="stylesheet" href="https://fonts.googleapis.com/css2?family=Roboto:wght@700&family=Source+Sans+3:wght@400&display=swap">
<style>
  :root {
    --page-bg: #e9e9ea;
    --card-white: #ffffff;
    --brand-blue: #2d5fb4;
    --brand-green: #6db33f;
    --icon-green: #5faa3a;
    --text-blue: #2a59ad;
    --back-deep: #2f56a8;
    --back-light: #7fc0e6;
    --mark-green: #5fb83a;
    --mark-dark: #2f7d1f;
  }
  html, body {
    margin: 0;
    padding: 0;
    width: 1200px;
    height: 1000px;
    overflow: hidden;
    background: var(--page-bg);
  }
  .canvas {
    position: relative;
    width: 1200px;
    height: 1000px;
  }
  .card {
    position: absolute;
    left: 265px;
    width: 665px;
    height: 397px;
    box-shadow: 0 4px 14px rgba(0,0,0,0.25);
    overflow: hidden;
  }
  .card-front {
    top: 73px;
    background: var(--card-white);
  }
  .card-back {
    top: 532px;
    background: radial-gradient(ellipse 60% 70% at 58% 50%, var(--back-light) 0%, #4f86cb 45%, var(--back-deep) 100%);
  }
  .brand {
    position: absolute;
    display: flex;
    align-items: center;
    font-family: "Roboto", Arial, sans-serif;
    font-weight: 700;
  }
  .brand-front {
    left: 34px;
    top: 40px;
    gap: 16px;
  }
  .brand-dot {
    border-radius: 50%;
    flex: none;
  }
  .brand-front .brand-dot {
    width: 62px;
    height: 62px;
    background: var(--mark-green);
  }
  .brand-front .brand-name {
    font-size: 30px;
    color: var(--brand-blue);
    letter-spacing: -0.3px;
  }
  .person {
    position: absolute;
    left: 33px;
    top: 202px;
    font-family: "Roboto", Arial, sans-serif;
  }
  .person-name {
    font-weight: 700;
    font-size: 19px;
    color: var(--text-blue);
    letter-spacing: 0.4px;
    margin: 0;
  }
  .person-role {
    display: flex;
    align-items: center;
    gap: 10px;
    margin-top: 2px;
    font-family: "Source Sans 3", Arial, sans-serif;
    font-weight: 400;
    font-size: 17px;
    color: var(--brand-green);
  }
  .role-rule {
    width: 262px;
    height: 2px;
    background: linear-gradient(to right, var(--brand-green), rgba(109,179,63,0));
  }
  .contact-list {
    position: absolute;
    left: 33px;
    top: 280px;
    margin: 0;
    padding: 0;
    list-style: none;
    font-family: "Source Sans 3", Arial, sans-serif;
    font-size: 16.5px;
    color: var(--text-blue);
  }
  .contact-list li {
    display: flex;
    align-items: center;
    gap: 8px;
    height: 23px;
  }
  .contact-icon {
    width: 15px;
    height: 15px;
    fill: var(--icon-green);
    flex: none;
  }
  .mark-large {
    position: absolute;
    left: 455px;
    top: 140px;
    width: 210px;
    height: 210px;
    border-radius: 50%;
    background: radial-gradient(circle at 60% 35%, #a5dc4e 0%, var(--mark-green) 50%, var(--mark-dark) 100%);
  }
  .brand-back {
    left: 95px;
    top: 130px;
    gap: 22px;
  }
  .brand-back .brand-dot {
    width: 130px;
    height: 130px;
    background: #ffffff;
  }
  .brand-back .brand-name {
    font-size: 40px;
    color: #ffffff;
    letter-spacing: -0.3px;
  }
</style>
</head>
<body>
<main class="canvas">
  <section class="card card-front" aria-label="Business card front">
    <div class="brand brand-front">
      <span class="brand-dot"></span>
      <span class="brand-name">KJ Glimmer Cleaning</span>
    </div>

    <div class="person">
      <p class="person-name">Julien Marchetti</p>
      <div class="person-role"><span>Owner</span><span class="role-rule"></span></div>
    </div>

    <ul class="contact-list">
      <li>
        <svg class="contact-icon" viewBox="0 0 16 16" aria-hidden="true"><path d="M3 1.5l2.5 0 1.2 3-1.6 1.2c.8 1.8 2.3 3.3 4.2 4.2l1.2-1.6 3 1.2v2.5c0 .8-.7 1.5-1.5 1.5C6.6 13.5 2.5 9.4 1.5 4 1.5 2.2 2.2 1.5 3 1.5z"/></svg>
        <span>555.014.2398</span>
      </li>
      <li>
        <svg class="contact-icon" viewBox="0 0 16 16" aria-hidden="true"><path d="M1 3.5h14v9H1z M1.6 4l6.4 5 6.4-5" fill="var(--icon-green)" stroke="#fff" stroke-width="1"/></svg>
        <span>julien@kjglimmercleaning.com</span>
      </li>
      <li>
        <svg class="contact-icon" viewBox="0 0 16 16" aria-hidden="true"><circle cx="8" cy="8" r="7"/><path d="M1 8h14M8 1c-3 3.5-3 10.5 0 14M8 1c3 3.5 3 10.5 0 14M2.5 4.5h11M2.5 11.5h11" stroke="#fff" stroke-width="0.9" fill="none"/></svg>
        <span>kjglimmercleaning.com</span>
      </li>
      <li>
        <svg class="contact-icon" viewBox="0 0 16 16" aria-hidden="true"><path d="M8 0.8c-3 0-5 2.2-5 5 0 3.6 5 9.4 5 9.4s5-5.8 5-9.4c0-2.8-2-5-5-5z"/><circle cx="8" cy="5.8" r="1.9" fill="#fff"/></svg>
        <span>14 Larkspur Road Tarnwood VIC 3999</span>
      </li>
    </ul>

    <div class="mark-large" aria-hidden="true"></div>
  </section>

  <section class="card card-back" aria-label="Business card back">
    <div class="brand brand-back">
      <span class="brand-dot"></span>
      <span class="brand-name">KJ Glimmer Cleaning</span>
    </div>
  </section>
</main>
</body>
</html>
```